Business card for Chicago based Private Equity Company

We need a business card for our PE company called Crestline Holdings. We want a simple and clean, yet creative card design. The back side should reflect our logo. Also would like to see embossed ideas. Should reflect strength and growth. Our logo is attached. Also need editable file. Details are as follows for Business Card:

Dana Welmore Co-Founder 2750 Marlow Avenue Suite 410 Fernvale, IL 60914 http://www.crestlineholdingsllc.example (D) 630.555.0147 (C) 312.555.0182 (E) dw@crestlineholdingsllc.example

```html
<!DOCTYPE html>
<html lang="en">
<head>
<meta charset="utf-8">
<title>Crestline Holdings – Business Card</title>
<link rel="stylesheet" href="https://fonts.googleapis.com/css2?family=Quicksand:wght@500;600;700&display=swap">
<style>
  :root {
    --backdrop: #d4d5d7;
    --card-white: #ffffff;
    --ink: #111111;
    --muted: #555555;
    --accent: #b3202a;
    --card-black: #000000;
    --pattern-light: #262626;
    --pattern-dark: #0b0b0b;
    --reverse-text: #ffffff;
  }
  * { margin: 0; padding: 0; box-sizing: border-box; }
  html, body { width: 1200px; height: 1200px; overflow: hidden; }
  body {
    background: var(--backdrop);
    font-family: "Quicksand", sans-serif;
    color: var(--ink);
    position: relative;
  }
  .card { position: absolute; left: 228px; width: 742px; }
  .card-front { top: 170px; height: 422px; background: var(--card-white); }
  .front-band {
    position: absolute; left: 0; right: 0; bottom: 0; height: 24px;
    background: var(--card-black);
  }
  .brand {
    position: absolute; left: 27px;
    display: flex; align-items: center; gap: 14px;
  }
  .card-front .brand { top: 182px; }
  .brand-dot {
    width: 56px; height: 56px; border-radius: 50%; background: var(--ink); flex: none;
  }
  .brand-name { font-size: 24px; font-weight: 600; color: var(--ink); letter-spacing: 0.5px; white-space: nowrap; }
  .holder { position: absolute; right: 86px; top: 40px; text-align: right; }
  .holder-name { font-size: 40px; font-weight: 700; line-height: 1; letter-spacing: -0.3px; }
  .holder-title { font-size: 18px; font-weight: 500; color: var(--muted); margin-top: 8px; }
  .contact { position: absolute; left: 372px; list-style: none; font-size: 19px; font-weight: 600; white-space: nowrap; }
  .contact li { display: flex; align-items: center; gap: 10px; height: 27px; }
  .contact svg { width: 15px; height: 15px; flex: none; fill: var(--accent); }
  .icon-spacer { width: 15px; flex: none; }
  .contact-address { top: 198px; }
  .contact-lines { top: 272px; }
  .contact-lines li { height: 29px; }
  .card-back { top: 601px; height: 423px; background: var(--card-black); overflow: hidden; }
  .back-pattern {
    position: absolute; inset: 0;
    background: linear-gradient(180deg, var(--pattern-light) 0%, var(--pattern-dark) 100%);
    opacity: 0.85;
  }
  .card-back .brand { left: 457px; top: 241px; }
  .card-back .brand-dot { background: var(--reverse-text); width: 44px; height: 44px; }
  .card-back .brand-name { color: var(--reverse-text); font-size: 20px; }
  .back-url {
    position: absolute; right: 27px; bottom: 20px;
    font-size: 21px; font-weight: 600; color: var(--reverse-text); white-space: nowrap;
  }
</style>
</head>
<body>
  <section class="card card-front">
    <div class="brand">
      <span class="brand-dot"></span>
      <span class="brand-name">Crestline Holdings</span>
    </div>
    <div class="holder">
      <div class="holder-name">Dana Welmore</div>
      <div class="holder-title">CO-FOUNDER</div>
    </div>
    <ul class="contact contact-address">
      <li><svg viewBox="0 0 16 16"><path d="M8 1 1 7.5h2V15h4v-4h2v4h4V7.5h2z"/></svg>2750 Marlow Avenue Suite 410</li>
      <li><span class="icon-spacer"></span>Fernvale, IL 60914</li>
    </ul>
    <ul class="contact contact-lines">
      <li><svg viewBox="0 0 16 16"><path d="M3 2c1-1 2 0 3 2s-1 2-1 3 2 4 4 4 1-2 3-1 2 2 1 3-3 2-6 0S1 7 2 4z"/></svg>630.555.0147</li>
      <li><svg viewBox="0 0 16 16"><path d="M5 1h6a1 1 0 0 1 1 1v12a1 1 0 0 1-1 1H5a1 1 0 0 1-1-1V2a1 1 0 0 1 1-1zm1 2v6h4V3z"/></svg>312.555.0182</li>
      <li><svg viewBox="0 0 16 16"><path d="M1 3h14v1L8 9 1 4zm0 3 7 5 7-5v7H1z"/></svg>dw@crestlineholdingsllc.example</li>
      <li><svg viewBox="0 0 16 16"><path d="M8 1a7 7 0 1 0 0 14A7 7 0 0 0 8 1zm0 1.5c.8.9 1.4 2.3 1.6 4H6.4c.2-1.7.8-3.1 1.6-4zM5 6.5H2.7A5.5 5.5 0 0 1 6 2.8c-.6 1-.9 2.3-1 3.7zm6 0c-.1-1.4-.4-2.7-1-3.7a5.5 5.5 0 0 1 3.3 3.7zM2.7 8H5c.1 1.5.4 2.8 1 3.8A5.5 5.5 0 0 1 2.7 8zm3.7 0h3.2c-.2 1.7-.8 3-1.6 4-.8-1-1.4-2.3-1.6-4zm4.6 0h2.3a5.5 5.5 0 0 1-3.3 3.8c.6-1 .9-2.3 1-3.8z"/></svg>www.crestlineholdingsllc.example</li>
    </ul>
    <div class="front-band"></div>
  </section>

  <section class="card card-back">
    <div class="back-pattern" role="img" aria-label="Faint repeating brand pattern covering the card back"></div>
    <div class="brand">
      <span class="brand-dot"></span>
      <span class="brand-name">Crestline Holdings</span>
    </div>
    <div class="back-url">www.crestlineholdingsllc.example</div>
  </section>
</body>
</html>
```